Renewal of the Ferolanza SA Website

Ferolanza SA is a metal construction company active in industrial piping, boilermaking and metal framing. We would like to renew our site.

This website must be ready to work with Wordpress.

The site will contain the following pages: Home, skills, presentation, contact.

The site must reflect the field of the metal construction sector. It must be clear and easily understandable. The objective is not to win mandates with but to present the company and its capabilities.

I have inserted the pages of our old presentations, to describe our sector but we do not want to reuse these elements, we are waiting for your creativity to surprise us. In the 2nd phase we will complete with new images if necessary and texts

Target Market(s)

International companies in the food, chemical and pharmaceutical sectors

Industry/Entity Type

Alimentaire, pharma, chimie

Number of Pages Required

4 page

Font styles to use
Sans Serif

Colors
0054AA
0677BA
7BADD7
CADEEF
E8F1F8

Requirements
Must have
• It must contain at least the requested pages, images of illustrations, places for descriptions
Should not have
• Elements that appear or disappear, too flash,

```html
<!DOCTYPE html>
<html lang="en">
<head>
<meta charset="utf-8">
<title>Ferolanza SA – Metal Construction</title>
<link href="https://fonts.googleapis.com/css2?family=Roboto:wght@400;500;700&family=Roboto+Condensed:wght@400;500;700;800&display=swap" rel="stylesheet">
<style>
:root{
  --navy:#0b1661;
  --deep:#15209e;
  --royal:#1b3aa0;
  --title-blue:#0e1f8c;
  --band-top:#6a87cf;
  --band-bottom:#2448c6;
  --ring:#2c4fb6;
  --label:#1f2437;
  --footer:#1e2447;
  --white:#ffffff;
  --ink:#333a48;
  --line:#c9cdd6;
  --muted:#7b8190;
}
*{box-sizing:border-box;margin:0;padding:0}
html,body{width:1200px;height:2600px;overflow:hidden;background:#fff}
body{font-family:"Roboto",Arial,sans-serif;color:var(--ink)}
.canvas{position:relative;width:1200px;height:2600px;overflow:hidden}
.abs{position:absolute}

/* header */
.site-header{left:0;top:0;width:1200px;height:78px;background:var(--white)}
.brand{left:145px;top:18px;display:flex;align-items:center;gap:12px}
.brand-dot{width:40px;height:40px;border-radius:50%;background:var(--royal)}
.brand-name{font-family:"Roboto Condensed",Arial,sans-serif;font-weight:700;font-size:30px;color:var(--navy);letter-spacing:1px}
.main-nav{right:144px;top:30px;display:flex;gap:32px}
.main-nav a{font-family:"Roboto",Arial,sans-serif;font-weight:500;font-size:15px;color:#111;text-decoration:none;padding-bottom:4px}
.main-nav a.active{border-top:2px solid var(--navy);border-bottom:3px solid var(--navy);padding:1px 3px 3px}

/* hero */
.hero-photo{left:0;top:78px;width:1200px;height:541px;
  background:radial-gradient(ellipse 420px 380px at 600px 250px,#a9bfd6 0%,#8fa3b4 40%,#8b6a52 62%,#5a534e 80%,#3d3b3c 100%)}
.hero-band{left:0;top:618px;width:1200px;height:251px;background:linear-gradient(180deg,var(--band-top),var(--band-bottom))}
.hero-title{left:0;top:232px;width:1200px;text-align:center;font-family:"Roboto Condensed",Arial,sans-serif;font-weight:700;font-size:74px;color:var(--white);text-shadow:2px 3px 4px rgba(0,0,0,.45)}
.play{left:570px;top:341px}
.service{width:306px;height:306px;border-radius:50%;border:6px solid var(--ring);overflow:hidden;top:509px}
.service-photo{width:100%;height:100%}
.service-label{position:absolute;left:36px;bottom:0;width:222px;height:88px;background:var(--label);border-radius:110px 110px 0 0/60px 60px 0 0;
  display:flex;align-items:center;justify-content:center;text-align:center;color:var(--white);
  font-family:"Roboto Condensed",Arial,sans-serif;font-weight:700;font-size:19px;line-height:22px;padding-bottom:10px}

/* skills */
.skills-photo{left:0;top:869px;width:473px;height:490px;background:linear-gradient(135deg,#3a3f46 0%,#7a5037 45%,#b77a50 60%,#2f3238 100%)}
.skills-panel{left:473px;top:869px;width:727px;height:490px;background:var(--navy)}
.section-title{font-family:"Roboto Condensed",Arial,sans-serif;font-weight:700;font-size:54px;color:var(--white)}
.skills-title{left:541px;top:944px}
.skills-text{left:541px;top:1028px;width:512px;font-size:15.5px;line-height:25.7px;color:var(--white);text-align:justify}
.skills-text p+p{margin-top:10px}
.btn{display:flex;align-items:center;justify-content:center;width:147px;height:42px;background:var(--royal);color:var(--white);
  font-family:"Roboto Condensed",Arial,sans-serif;font-weight:700;font-size:18px;border-radius:3px}
.read-more{left:541px;top:1242px}

/* presentation + contact background */
.lower-photo{left:0;top:1358px;width:1200px;height:1082px;background:linear-gradient(180deg,#2a3ea8 0%,#6fa6dc 45%,#3f6fb6 70%,#2a4f95 100%)}
.curve{left:0;top:0}
.presentation-title{left:0;top:1402px;width:1200px;text-align:center}
.slide{top:1508px;width:300px;height:213px;background:var(--white);padding:5px}
.slide-page{width:100%;height:100%;background:linear-gradient(90deg,#6aa6de 0 40%,#e8f1f8 40% 100%)}
.arrows{left:556px;top:1779px;display:flex;gap:10px}

/* contact */
.contact-card{left:144px;top:1982px;width:912px;height:393px;background:var(--white)}
.contact-title{left:0;top:2025px;width:1200px;text-align:center;color:var(--title-blue)}
.info{left:188px;display:flex;gap:22px}
.info-icon{width:44px;height:44px;flex:none}
.info h4{font-family:"Roboto Condensed",Arial,sans-serif;font-weight:500;font-size:14px;color:#222;margin-bottom:4px}
.info p{font-family:"Roboto Condensed",Arial,sans-serif;font-size:14px;line-height:19px;color:#222}
.field{left:438px;width:277px;height:43px;border:1px solid var(--line);display:flex;align-items:center;justify-content:space-between;padding:0 16px;
  font-family:"Roboto Condensed",Arial,sans-serif;font-size:14px;color:var(--muted)}
.message{left:735px;top:2120px;width:277px;height:147px;align-items:flex-start;padding-top:14px}
.submit{left:735px;top:2277px}

/* footer */
.site-footer{left:0;top:2440px;width:1200px;height:160px;background:var(--footer)}
.footer-brand{left:145px;top:2508px;display:flex;align-items:center;gap:14px}
.footer-brand .brand-name{color:var(--white);font-size:38px}
.footer-brand .brand-dot{background:#9aa6c9;width:52px;height:52px}
.social{left:592px;top:2493px;display:flex;gap:14px}
.social span{width:30px;height:30px;border-radius:50%;background:var(--white)}
.legal{left:592px;top:2546px;font-size:16px;color:var(--white)}
</style>
</head>
<body>
<div class="canvas">

  <header class="site-header abs">
    <div class="brand abs"><span class="brand-dot"></span><span class="brand-name">FEROLANZA SA</span></div>
    <nav class="main-nav abs">
      <a class="active" href="#">HOME</a><a href="#">SKILLS</a><a href="#">PRESENTATION</a><a href="#">CONTACT</a>
    </nav>
  </header>

  <div class="hero-photo abs" role="img" aria-label="View through a large concrete pipe onto a pipeline trench under a cloudy sky"></div>
  <div class="hero-band abs"></div>
  <h1 class="hero-title abs">INDUSTRIAL PIPING</h1>
  <svg class="play abs" width="60" height="60" viewBox="0 0 60 60">
    <circle cx="30" cy="30" r="27" fill="#fff"/>
    <circle cx="30" cy="30" r="22" fill="#1f3a9c"/>
    <path d="M25 19 L40 30 L25 41 Z" fill="#fff"/>
  </svg>

  <div class="service abs" style="left:143px">
    <div class="service-photo" role="img" aria-label="Refinery with insulated pipe runs" style="background:linear-gradient(160deg,#b8cde4,#7c8da0 55%,#3d4653)"></div>
    <div class="service-label">INDUSTRIAL<br>PIPING</div>
  </div>
  <div class="service abs" style="left:447px">
    <div class="service-photo" role="img" aria-label="Boilermaker in a hard hat working on a flange" style="background:linear-gradient(160deg,#5b6068,#8b6a48 50%,#2b3140)"></div>
    <div class="service-label">BOILER MAKING</div>
  </div>
  <div class="service abs" style="left:753px">
    <div class="service-photo" role="img" aria-label="Blue steel frame structure under a clear sky" style="background:linear-gradient(180deg,#a8c6ea,#4f79c2 55%,#22407f)"></div>
    <div class="service-label">METAL FRAMING</div>
  </div>

  <div class="skills-photo abs" role="img" aria-label="Copper pipes and valves in a plant room"></div>
  <section class="skills-panel abs"></section>
  <h2 class="section-title skills-title abs">SKILLS</h2>
  <div class="skills-text abs">
    <p>Sed ut perspiciatis unde omnis iste natus error sit voluptatem accusantium doloremque laudantium, totam rem aperiam, eaque ipsa quae ab illo inventore veritatis et quasi architecto beatae vitae dicta sunt explicabo. Nemo enim ipsam voluptatem quia voluptas sit aspernatur aut odit aut fugit</p>
    <p>Eque ipsa quae ab illo inventore veritatis et quasi architecto beatae vitae dicta sunt explicabo. Nemo enim ipsam voluptatem quia voluptas sit aspernatur aut odit aut fugit</p>
  </div>
  <a class="btn read-more abs">READ MORE</a>

  <div class="lower-photo abs" role="img" aria-label="Industrial plant with large blue pipelines"></div>
  <svg class="curve abs" width="1200" height="2600" viewBox="0 0 1200 2600">
    <path d="M0 1358 H1200 V1865 Q900 1915 600 1906 Q180 1890 0 1730 Z" fill="#15209e" fill-opacity="0.9"/>
  </svg>
  <h2 class="section-title presentation-title abs">PRESENTATION</h2>
  <div class="slide abs" style="left:139px"><div class="slide-page" role="img" aria-label="Brochure page on industrial piping for the chemical sector"></div></div>
  <div class="slide abs" style="left:450px"><div class="slide-page" role="img" aria-label="Brochure page on industrial piping for the food sector"></div></div>
  <div class="slide abs" style="left:761px"><div class="slide-page" role="img" aria-label="Brochure page on industrial piping for the chemical sector"></div></div>
  <div class="arrows abs">
    <svg width="40" height="40" viewBox="0 0 40 40"><circle cx="20" cy="20" r="18" fill="none" stroke="#aab4e6" stroke-width="2"/><path d="M28 20 H12 M18 13 L11 20 L18 27" fill="none" stroke="#aab4e6" stroke-width="2"/></svg>
    <svg width="40" height="40" viewBox="0 0 40 40"><circle cx="20" cy="20" r="18" fill="none" stroke="#aab4e6" stroke-width="2"/><path d="M12 20 H28 M22 13 L29 20 L22 27" fill="none" stroke="#aab4e6" stroke-width="2"/></svg>
  </div>

  <section class="contact-card abs"></section>
  <h2 class="section-title contact-title abs">CONTACT</h2>

  <div class="info abs" style="top:2123px">
    <svg class="info-icon" viewBox="0 0 44 44"><circle cx="22" cy="22" r="20.5" fill="none" stroke="#1b3aa0" stroke-width="1.5"/><path d="M22 32 C16 25 14 22 14 18.5 A8 8 0 0 1 30 18.5 C30 22 28 25 22 32 Z" fill="none" stroke="#1b3aa0" stroke-width="1.5"/><circle cx="22" cy="18.5" r="3" fill="none" stroke="#1b3aa0" stroke-width="1.5"/></svg>
    <div><h4>LOCATION</h4><p>343,minim veniam, quis nostrud<br>exercitation ullamco</p></div>
  </div>
  <div class="info abs" style="top:2207px">
    <svg class="info-icon" viewBox="0 0 44 44"><circle cx="22" cy="22" r="20.5" fill="none" stroke="#1b3aa0" stroke-width="1.5"/><rect x="12" y="15" width="20" height="14" fill="none" stroke="#1b3aa0" stroke-width="1.5"/><path d="M12 15 L22 23 L32 15" fill="none" stroke="#1b3aa0" stroke-width="1.5"/></svg>
    <div><h4>EMAIL US</h4><p>info@ferolanza.com</p></div>
  </div>
  <div class="info abs" style="top:2273px">
    <svg class="info-icon" viewBox="0 0 44 44"><circle cx="22" cy="22" r="20.5" fill="none" stroke="#1b3aa0" stroke-width="1.5"/><path d="M15 13 L19 13 L21 18 L18.5 20 C19.5 23 21 24.5 24 25.5 L26 23 L31 25 L31 29 C31 30 30 31 29 31 C20 30.5 13.5 24 13 15 C13 14 14 13 15 13 Z" fill="none" stroke="#1b3aa0" stroke-width="1.5"/></svg>
    <div><h4>CONTACT US</h4><p style="font-size:15px">+ 1 888 888 8888</p></div>
  </div>

  <div class="field abs" style="top:2120px">First Name<svg width="10" height="12" viewBox="0 0 10 12"><rect x="2" y="1" width="6" height="10" fill="none" stroke="#555"/></svg></div>
  <div class="field abs" style="top:2172px">Email<svg width="12" height="10" viewBox="0 0 12 10"><rect x="1" y="1" width="10" height="8" fill="none" stroke="#555"/><path d="M1 1 L6 5 L11 1" fill="none" stroke="#555"/></svg></div>
  <div class="field abs" style="top:2225px">Phone No<svg width="10" height="10" viewBox="0 0 10 10"><path d="M1 2 L3 1 L4.5 3.5 L3.5 4.5 C4 5.5 4.5 6 5.5 6.5 L6.5 5.5 L9 7 L8 9 C4 8.5 1.5 6 1 2 Z" fill="#555"/></svg></div>
  <div class="field abs" style="top:2277px">Post Code<svg width="8" height="11" viewBox="0 0 8 11"><path d="M4 11 C1 7 0.5 5.5 0.5 4 A3.5 3.5 0 0 1 7.5 4 C7.5 5.5 7 7 4 11 Z" fill="#555"/><circle cx="4" cy="4" r="1.3" fill="#fff"/></svg></div>
  <div class="field message abs">Message<svg width="13" height="11" viewBox="0 0 13 11"><ellipse cx="6.5" cy="5" rx="5.5" ry="3.8" fill="none" stroke="#555"/><path d="M3 8 L2 10.5 L5.5 8.6" fill="#555"/></svg></div>
  <a class="btn submit abs">SUBMIT</a>

  <footer class="site-footer abs"></footer>
  <div class="footer-brand abs"><span class="brand-dot"></span><span class="brand-name">FEROLANZA SA</span></div>
  <div class="social abs"><span></span><span></span></div>
  <p class="legal abs">© 2023.Ferolanza.All Rights reserved &nbsp;|&nbsp; Privacy &nbsp;|&nbsp; Terms of Use</p>

</div>
</body>
</html>
```